Business Card Design Project - KLB

I am looking for a more sophisticated card design for my company,
"The Kestrel Bureau"

We are a consultancy focused on strategy and change in Associations and professional organisations.

I am a lawyer and psychologist with a PhD and so am looking for something that communicates seriousness and credibility but also quirky creative solutions for strategic problems, which is my field of speciality.

I am looking for something that is quietly spoken, rather than loud colours ('credible' and 'creative' are the two adjectives that I think of as competing here).

I particularly like an embossed card style - heavy white card with plain white or white and black or white and grey text.

The key logo image for the company is a question mark and I am open to suggestions and ideas on design.

I have attached a file that includes a couple of styles that have caught my eye and my thoughts on them. Hopefully they communicate what I'm looking for.
Updates

Thank you for all the great suggestions and designs.

I really appreciated the effort and creative energy you put into your designs. I have now closed the project after selecting a design and advising the successful designer of the card that I am happy with.

Regards

Target Market(s)

Organisations (CEO's and Boards), Governments, Legal professionals, Membership Associations and aspiring professionals.

Industry/Entity Type

Lawyer

Requirements
Must have
• The key logo element is a question mark (?) and this needs to be incorporated.

Embossed style - cut outs or other design ideas interest me too.

The attached file has a number of sample ideas and comments on each one that I like.
Should not have
• I like crisp, modern fonts (Myriads etc...) and do not like embellished fonts or Times etc...

```html
<!DOCTYPE html>
<html lang="en">
<head>
<meta charset="utf-8">
<title>The Kestrel Bureau – Business Card</title>
<link rel="stylesheet" href="https://fonts.googleapis.com/css2?family=Mulish:wght@400;600;700&display=swap">
<style>
  :root {
    --backdrop: #e9e6e3;
    --card: #ffffff;
    --card-edge: #d4d0cc;
    --ink: #3a3a3a;
    --ink-soft: #4a4a4a;
    --mark-grey: #a9a9aa;
    --mark-light: #bdbdbe;
  }
  html, body {
    margin: 0;
    width: 1200px;
    height: 900px;
    overflow: hidden;
    background: var(--backdrop);
    font-family: "Mulish", "Helvetica Neue", Arial, sans-serif;
  }
  .stage {
    position: relative;
    width: 1200px;
    height: 900px;
  }
  .card {
    position: absolute;
    top: 295px;
    width: 540px;
    height: 310px;
    background: var(--card);
    box-shadow: 0 0 0 1px var(--card-edge), 0 6px 18px rgba(0,0,0,0.12);
    overflow: hidden;
    color: var(--ink);
  }
  .card--front { left: 40px; }
  .card--back { left: 620px; }

  /* Front */
  .brand {
    position: absolute;
    left: 20px;
    top: 32px;
    width: 220px;
    text-align: center;
  }
  .brand__dot {
    width: 122px;
    height: 122px;
    margin: 0 auto;
    border-radius: 50%;
    background: var(--mark-light);
  }
  .brand__name {
    margin-top: 48px;
    font-size: 20px;
    font-weight: 700;
    color: var(--ink);
    letter-spacing: 0.2px;
  }
  .details {
    position: absolute;
    left: 308px;
    top: 66px;
    font-size: 14px;
    line-height: 18px;
    color: var(--ink-soft);
  }
  .details__person {
    font-weight: 700;
    color: var(--ink);
    margin: 0 0 18px;
  }
  .details__address { margin: 0 0 18px; }
  .contact { margin: 0; padding: 0; list-style: none; }
  .contact__label {
    display: inline-block;
    width: 20px;
    font-weight: 700;
    color: var(--ink);
  }

  /* Back */
  .accent-circle {
    position: absolute;
    left: 268px;
    top: -14px;
    width: 272px;
    height: 272px;
    border-radius: 50%;
    background: var(--mark-grey);
  }
  .back__name {
    position: absolute;
    left: 0;
    width: 280px;
    top: 134px;
    text-align: center;
    font-size: 26px;
    font-weight: 700;
    color: var(--ink);
  }
  .back__web {
    position: absolute;
    left: 0;
    width: 280px;
    top: 176px;
    text-align: center;
    font-size: 16px;
    color: var(--ink-soft);
  }
</style>
</head>
<body>
<main class="stage">
  <section class="card card--front" aria-label="Card front">
    <div class="brand">
      <div class="brand__dot"></div>
      <div class="brand__name">Kestrel Bureau</div>
    </div>
    <div class="details">
      <p class="details__person">Dr. Mara Ellison<br>Director</p>
      <p class="details__address">The Kestrel Bureau<br>P.O. Box 4180, Linden Vale,<br>Sydney, Australia</p>
      <ul class="contact">
        <li><span class="contact__label">M</span>+61455 210 734</li>
        <li><span class="contact__label">P</span>+612 9460 2175</li>
        <li><span class="contact__label">E</span>mara@kestrelbureau.com.au</li>
      </ul>
    </div>
  </section>

  <section class="card card--back" aria-label="Card back">
    <div class="accent-circle"></div>
    <div class="back__name">Kestrel Bureau</div>
    <div class="back__web">www.kestrelbureau.com.au</div>
  </section>
</main>
</body>
</html>
```